A2サイズのLED型看板がありその内容の変更です。今回の内容は少し難しいかとおもいますが、宜しくお願い致します。当社は自社ビルで1Fが駐車場で2Fがストレッチ専門店、3~5Fがトレーニングスタジオでトレーニングスタジオの受付は4Fです。A2の中に この2つの内容(パーソナルトレーニングとストレッチ)をあまりごちゃごちゃせずに伝えて頂ければと思っております。
下記をご参考いただければと思います。

法人名は、ミナレクス株式会社
店舗名 4Fトレーニングスタジオナベロ
HP   http://www.k-navelo.jp
http://navelo.net

店舗名 2Fストレッチ専門店 ルミナスカイアークストレッチ
HP  https://www.k-navelo.jp/stretch

写真素材などは別途添付してます。
店舗名/電話番号/ロゴ 受付階
ロゴデータです。
電話番号は、特に表示しなくても良いです。
ビルの何階に何があるのかをわかるようにして頂ければと思います。
やはり、2つあるとごちゃごちゃして少し難しいかと思いますが、トレーニング
とストレッチがわかるような感じと体験についての表記などがあれば良いと
思いますので宜しくお願い致します。
一応、袖にパンフレットをぶら下げておくので興味をもたれた方はパンフを取りたくなるような感じでもお願い致します。
少し、難しくてすみません。。。宜しくお願い致します。

色合いとイメージがピッタリと来ました。ありがとうございました。

この度は、沢山の方からのご提案頂きましてありがとうございました。
また、何かありましたらご提案いただければと思っております。
ありがとうございました。

```html
<!DOCTYPE html>
<html lang="ja">
<head>
<meta charset="utf-8">
<title>ナベロ / ルミナスカイアークストレッチ フロア案内</title>
<link rel="stylesheet" href="https://fonts.googleapis.com/css2?family=Noto+Serif+JP:wght@700;900&family=Noto+Sans+JP:wght@500;700;900&display=swap">
<style>
  :root {
    --studio-green: #45ad32;
    --studio-green-dark: #2f8f25;
    --stretch-pink: #e3147f;
    --stretch-pink-dark: #b80c63;
    --parking-taupe: #9c8c7b;
    --parking-taupe-dark: #7d6e5f;
    --callout-yellow: #ffe21a;
    --ink: #1d1d1d;
    --white: #ffffff;
  }
  * { margin: 0; padding: 0; box-sizing: border-box; }
  html, body { width: 850px; height: 1200px; overflow: hidden; background: var(--white); }
  .signboard {
    position: relative;
    width: 850px;
    height: 1200px;
    overflow: hidden;
    background: var(--white);
    font-family: "Noto Sans JP", sans-serif;
  }

  /* Training studio block */
  .studio-band {
    position: absolute; left: 0; top: 0; width: 850px; height: 420px;
    background: linear-gradient(180deg, var(--studio-green) 0%, var(--studio-green) 75%, rgba(69,173,50,0) 100%);
  }
  .studio-photo {
    position: absolute; right: 0; top: 0; width: 420px; height: 415px;
    background: linear-gradient(160deg, #d9d2cb 0%, #c7b3a6 40%, #e9e4df 75%, rgba(255,255,255,0) 100%);
  }

  /* Stretch block */
  .stretch-band {
    position: absolute; left: 0; top: 520px; width: 850px; height: 400px;
    background: linear-gradient(180deg, var(--stretch-pink) 0%, var(--stretch-pink) 80%, rgba(227,20,127,0) 100%);
  }
  .stretch-photo {
    position: absolute; right: 0; top: 520px; width: 420px; height: 390px;
    background: linear-gradient(150deg, #e6c9c0 0%, #c98d8c 45%, #efe2de 80%, rgba(255,255,255,0) 100%);
  }

  .floor-tag {
    position: absolute; left: 22px; width: 96px;
    display: flex; flex-direction: column; align-items: center; justify-content: center;
    color: var(--white); font-weight: 900; line-height: 1;
  }
  .floor-tag .floor { font-size: 58px; letter-spacing: -1px; }
  .floor-tag .note { font-size: 24px; margin-top: 4px; }
  .floor-tag--studio { background: var(--studio-green-dark); border: 3px solid var(--white); }
  .floor-tag--stretch { background: var(--stretch-pink-dark); border: 3px solid var(--white); }
  .floor-tag--parking { background: var(--parking-taupe-dark); border: 3px solid var(--white); }

  .offer {
    position: absolute; left: 150px;
    color: var(--white); font-family: "Noto Serif JP", serif; font-weight: 900;
    font-size: 44px; letter-spacing: 1px; white-space: nowrap;
    text-shadow: 0 2px 6px rgba(0,0,0,0.15);
  }
  .offer small { font-size: 24px; font-weight: 700; }
  .headline {
    position: absolute; left: 140px;
    color: var(--white); font-family: "Noto Serif JP", serif; font-weight: 900;
    line-height: 1.08; white-space: nowrap;
    text-shadow: 0 2px 6px rgba(0,0,0,0.18);
  }
  .headline--studio { top: 112px; font-size: 100px; }
  .headline--stretch { top: 604px; font-size: 96px; }

  .brand {
    position: absolute; left: 0; width: 850px;
    display: flex; align-items: center; justify-content: center; gap: 18px;
    font-family: "Noto Sans JP", sans-serif; font-weight: 900; white-space: nowrap; line-height: 1;
  }
  .brand .mark { border-radius: 50%; flex: none; }
  .brand--studio { top: 432px; height: 70px; font-size: 62px; color: var(--studio-green-dark); letter-spacing: 4px; }
  .brand--studio .mark { width: 44px; height: 44px; background: var(--studio-green); }
  .brand--stretch { top: 946px; height: 60px; left: 50px; width: auto; justify-content: flex-start; font-size: 40px; color: var(--stretch-pink-dark); }
  .brand--stretch .mark { width: 32px; height: 32px; border-radius: 0; background: var(--stretch-pink); }

  /* Parking block */
  .parking-band {
    position: absolute; left: 0; top: 1060px; width: 850px; height: 140px;
    background: var(--parking-taupe);
  }
  .parking-text {
    position: absolute; left: 150px; top: 1088px; width: 520px; text-align: center;
    color: var(--white); font-family: "Noto Serif JP", serif; font-weight: 900;
    font-size: 80px; line-height: 1; letter-spacing: 4px;
  }

  .brochure-callout {
    position: absolute; left: 692px; top: 932px; width: 150px; height: 150px;
  }
  .brochure-callout svg { position: absolute; inset: 0; width: 100%; height: 100%; }
  .brochure-callout p {
    position: absolute; inset: 0;
    display: flex; flex-direction: column; align-items: center; justify-content: center;
    color: var(--ink); font-weight: 900; text-align: center; line-height: 1.25;
  }
  .brochure-callout .lead { font-size: 20px; }
  .brochure-callout .sub { font-size: 16px; }
</style>
</head>
<body>
<main class="signboard">

  <section class="studio">
    <div class="studio-band"></div>
    <div class="studio-photo" role="img" aria-label="トレーニングスタジオでトレーナーと女性がポーズをとる写真"></div>

    <div class="floor-tag floor-tag--studio" style="top:30px;height:92px;"><span class="floor">5F</span></div>
    <div class="floor-tag floor-tag--studio" style="top:136px;height:116px;"><span class="floor">4F</span><span class="note">受付</span></div>
    <div class="floor-tag floor-tag--studio" style="top:266px;height:92px;"><span class="floor">3F</span></div>

    <p class="offer" style="top:36px;">体験料3000円<small>/30分</small></p>
    <h1 class="headline headline--studio">トレーニング<br>スタジオ</h1>

    <div class="brand brand--studio"><span class="mark"></span>NAVELO</div>
  </section>

  <section class="stretch">
    <div class="stretch-band"></div>
    <div class="stretch-photo" role="img" aria-label="施術者が女性の体をストレッチしている写真"></div>

    <div class="floor-tag floor-tag--stretch" style="top:672px;height:100px;"><span class="floor">2F</span></div>

    <p class="offer" style="top:540px;">初回お試し15分無料</p>
    <h2 class="headline headline--stretch">ストレッチ<br>専門店</h2>

    <div class="brand brand--stretch"><span class="mark"></span>ルミナスカイアークストレッチ</div>
  </section>

  <section class="parking">
    <div class="parking-band"></div>
    <div class="floor-tag floor-tag--parking" style="top:1082px;height:96px;"><span class="floor">1F</span></div>
    <p class="parking-text">駐車場完備</p>
  </section>

  <aside class="brochure-callout">
    <svg viewBox="0 0 180 180" aria-hidden="true">
      <polygon fill="#ffe21a" stroke="#1d1d1d" stroke-width="2"
        points="178,90 163.4,109.7 166.2,134 143.7,143.7 134,166.2 109.7,163.4 90,178 70.3,163.4 46,166.2 36.3,143.7 13.8,134 16.6,109.7 2,90 16.6,70.3 13.8,46 36.3,36.3 46,13.8 70.3,16.6 90,2 109.7,16.6 134,13.8 143.7,36.3 166.2,46 163.4,70.3"/>
    </svg>
    <p><span class="lead">パンフレット</span><span class="sub">ご自由に</span><span class="sub">お取り下さい</span></p>
  </aside>

</main>
</body>
</html>
```